Wren Sporting Goods Inc.

Need to create a website that is informational and has the ability to sell goods and services. Such as a custom t shirt designer where the user can upload and image to be displayed on the garmet. The sports we specialize in are basketball, football, and baseball.

Would like like:
Home Page
Locker Room Page:
Custom Uniforms Page
Custom Shirt Creator
Brands
About

Competitor websites are
tundrafieldwearnx.com
dvq.com
lumarogear.com

```html
<!DOCTYPE html>
<html lang="en">
<head>
<meta charset="utf-8">
<title>Wren Sporting Goods — Custom Sports Apparel</title>
<link href="https://fonts.googleapis.com/css2?family=Outfit:wght@400;500;600;700;800;900&display=swap" rel="stylesheet">
<style>
:root{
  --blue:#2262b4;
  --blue-footer:#1f5fb3;
  --red:#cc4541;
  --red-btn:#cf3f3b;
  --ink:#111111;
  --muted:#3b3b3b;
  --hero-bg:#dde3df;
  --card-bg:#f5f4ee;
  --line:#d4d4d4;
  --white:#ffffff;
}
*{box-sizing:border-box;margin:0;padding:0}
html,body{width:1200px;height:3916px;overflow:hidden}
body{font-family:"Outfit",sans-serif;color:var(--ink);background:var(--white);position:relative}
.abs{position:absolute}
.btn{position:absolute;display:flex;align-items:center;justify-content:center;color:var(--white);font-weight:600;font-size:13px;height:39px;padding:0 20px}
.btn-blue{background:var(--blue)}
.btn-red{background:var(--red-btn)}
.h2{font-weight:800;font-size:34px;line-height:1.2;text-transform:uppercase;letter-spacing:-.3px}
.para{font-size:12.5px;line-height:1.55;color:var(--muted)}
.ph{position:absolute}

/* header */
.site-header{position:absolute;left:0;top:0;width:1200px;height:76px;background:var(--white)}
.brand{position:absolute;display:flex;align-items:center;gap:8px;font-weight:800;color:var(--red)}
.brand .mark{border-radius:50%;background:var(--blue)}
.main-nav{position:absolute;right:215px;top:28px;display:flex;gap:0;font-size:13px;color:#333}
.main-nav span{padding:0 18px;border-left:1px solid #444;line-height:14px}
.main-nav span:first-child{border-left:none}

/* hero */
.hero{position:absolute;left:0;top:76px;width:1200px;height:608px;background:var(--hero-bg);overflow:hidden}
.hero h1{position:absolute;left:75px;top:158px;font-size:50px;font-weight:900;line-height:57px;text-transform:uppercase;letter-spacing:-.5px}
.hero h1 .outline{color:transparent;-webkit-text-stroke:1.6px var(--red)}
.hero .para{position:absolute;left:75px;top:336px;width:330px;font-size:12.5px}
.scroll-down{position:absolute;right:75px;top:550px;font-size:13px;font-weight:500}

/* sports */
.sport-card{position:absolute;top:830px;width:248px;height:220px;background:var(--card-bg)}
.sport-card .ball{position:absolute;left:64px;top:35px;width:120px;height:120px;border-radius:50%}
.sport-card .label{position:absolute;left:0;right:0;top:184px;text-align:center;font-weight:800;font-size:19px}

/* trust band */
.trust{position:absolute;left:0;top:1975px;width:1200px;height:356px;background:var(--red)}
.trust .h2{position:absolute;left:0;right:0;top:56px;text-align:center;color:var(--white)}
.feature{position:absolute;top:168px;width:190px;text-align:center;color:var(--white);font-weight:700;font-size:14px}
.feature .icon{width:62px;height:62px;margin:0 auto 14px;border:2px solid var(--white);background:var(--blue);display:flex;align-items:center;justify-content:center;box-shadow:0 0 0 3px var(--white) inset}
.dash{position:absolute;top:199px;height:0;border-top:1.5px dashed rgba(255,255,255,.85)}

/* brands */
.brand-badge{position:absolute;top:2898px;width:148px;height:148px;border-radius:50%;border:1.5px dashed;display:flex;align-items:center;justify-content:center;gap:8px;font-size:24px;font-weight:500;background:#f7f7fb}
.brand-badge .dot{width:22px;height:22px;border-radius:50%}

/* footer */
.site-footer{position:absolute;left:0;top:3557px;width:1200px;height:359px;background:var(--blue-footer);color:var(--white)}
.footer-nav{position:absolute;left:0;right:0;top:183px;display:flex;justify-content:center;font-size:13px}
.footer-nav span{padding:0 18px;border-left:1px solid var(--white);line-height:14px}
.footer-nav span:first-child{border-left:none}
.socials{position:absolute;left:0;right:0;top:228px;display:flex;justify-content:center;gap:9px}
.socials span{width:34px;height:34px;border-radius:50%;background:var(--red)}
.footer-rule{position:absolute;left:75px;right:75px;top:310px;border-top:1px solid rgba(255,255,255,.6)}
.copyright{position:absolute;left:0;right:0;top:326px;text-align:center;font-size:12px}
.to-top{position:absolute;left:1138px;top:3841px;width:44px;height:44px;border-radius:50%;background:var(--red);display:flex;align-items:center;justify-content:center}
</style>
</head>
<body>

<header class="site-header">
  <div class="brand" style="left:75px;top:20px;font-size:21px;">
    <span class="mark" style="width:20px;height:20px;"></span>
    <span>Wren Sporting Goods</span>
  </div>
  <nav class="main-nav">
    <span>Home</span><span>Locker Room</span><span>Custom Uniforms</span><span>Custom Shirt Creator</span><span>Brands</span><span>About Us</span>
  </nav>
  <div class="btn btn-blue" style="left:1011px;top:18px;width:114px;">Shop Now</div>
</header>

<section class="hero">
  <div class="ph" role="img" aria-label="Athlete in a red zip top holding a basketball on her shoulder" style="left:478px;top:0;width:722px;height:608px;background:linear-gradient(120deg,#d7dcd8 0%,#c8ccc8 35%,#d9482f 55%,#c23a25 100%);"></div>
  <h1>Custom <span class="outline">Sports</span><br>Apparel Built For<br>Champions</h1>
  <p class="para">Premium custom uniforms, team gear, and personalized apparel for Basketball, Football, and Baseball.</p>
  <div class="btn btn-blue" style="left:75px;top:399px;width:158px;">Design Your Uniform</div>
  <div class="btn btn-red" style="left:240px;top:399px;width:158px;">Create Custom Shirt</div>
  <div class="scroll-down">Scroll Down</div>
</section>

<section class="sports">
  <h2 class="h2 abs" style="left:0;right:0;top:765px;text-align:center;">Sports We Serve</h2>
  <div class="sport-card" style="left:192px;">
    <div class="ball" role="img" aria-label="Basketball" style="background:radial-gradient(circle at 35% 30%,#e08a4a,#b4531f 70%);"></div>
    <div class="label">BASKETBALL</div>
  </div>
  <div class="sport-card" style="left:476px;">
    <div class="ball" role="img" aria-label="Soccer ball" style="background:radial-gradient(circle at 35% 30%,#ffffff,#d9d3d3 55%,#b7262c 100%);"></div>
    <div class="label">FOOTBALL</div>
  </div>
  <div class="sport-card" style="left:760px;">
    <div class="ball" role="img" aria-label="Baseball" style="background:radial-gradient(circle at 35% 30%,#ffffff,#e3e2df 70%);"></div>
    <div class="label">BASEBALL</div>
  </div>
  <div class="abs" style="left:75px;top:1125px;width:1050px;border-top:1px solid var(--line);"></div>
</section>

<section class="uniforms">
  <div class="ph" role="img" aria-label="Baseball player in cap and dark jersey adjusting his glove" style="left:75px;top:1218px;width:459px;height:530px;background:linear-gradient(180deg,#8fb0b4 0%,#6b8d92 45%,#1d1c1d 75%,#141414 100%);"></div>
  <h2 class="h2 abs" style="left:595px;top:1236px;width:500px;">Custom Team Uniforms Made Easy</h2>
  <p class="para abs" style="left:595px;top:1328px;width:480px;">Complete uniform solutions for your team — colors, logos, names, and numbers all under your control. Perfect for schools, clubs, and leagues.</p>
  <div class="btn btn-blue" style="left:595px;top:1386px;width:176px;">Start Your Team Order</div>
  <div class="ph" role="img" aria-label="Basketball players in orange kits dribbling on an indoor court" style="left:595px;top:1475px;width:529px;height:400px;background:linear-gradient(160deg,#c9c4bb 0%,#a85a3e 45%,#8a4a32 70%,#c2906b 100%);"></div>
</section>

<section class="trust">
  <h2 class="h2">Trusted By Teams, Built For<br>Performance</h2>
  <div class="dash" style="left:277px;width:173px;"></div>
  <div class="dash" style="left:512px;width:174px;"></div>
  <div class="dash" style="left:748px;width:173px;"></div>
  <div class="feature" style="left:151px;">
    <div class="icon"><svg width="28" height="28" viewBox="0 0 28 28" fill="none" stroke="#fff" stroke-width="2"><path d="M9 4l-6 4 3 5 3-2v13h10V11l3 2 3-5-6-4c-1 2-3 3-5 3s-4-1-5-3z"/></svg></div>
    TEAM UNIFORMS
  </div>
  <div class="feature" style="left:386px;">
    <div class="icon"><svg width="28" height="28" viewBox="0 0 28 28" fill="none" stroke="#fff" stroke-width="2"><rect x="5" y="4" width="18" height="8"/><rect x="3" y="12" width="22" height="8"/><path d="M8 20v5h12v-5"/></svg></div>
    CUSTOM PRINTING
  </div>
  <div class="feature" style="left:622px;">
    <div class="icon"><svg width="28" height="28" viewBox="0 0 28 28" fill="none" stroke="#fff" stroke-width="2"><path d="M14 3l9 4v7c0 6-4 9-9 11-5-2-9-5-9-11V7z"/><path d="M10 14l3 3 5-6"/></svg></div>
    TRUSTED BRANDS
  </div>
  <div class="feature" style="left:857px;">
    <div class="icon"><svg width="28" height="28" viewBox="0 0 28 28" fill="none" stroke="#fff" stroke-width="2"><circle cx="16" cy="15" r="8"/><path d="M16 10v5l3 2M14 4h4M2 12h5M3 16h4M4 20h4"/></svg></div>
    FAST TURNAROUND
  </div>
</section>

<section class="design">
  <h2 class="h2 abs" style="left:126px;top:2440px;width:460px;">Design It. Preview It.<br>Wear It.</h2>
  <p class="para abs" style="left:126px;top:2536px;width:460px;">Bring your ideas to life with our easy-to-use Custom Shirt Creator. Whether you're designing for your team, a special event, or personal use, our platform gives you full control over every detail. Upload your own logos or images, add names, numbers, or slogans, and see a real-time preview of how your design will look on your chosen garment. Once you're happy with your creation, place your order instantly and get high-quality, custom apparel delivered straight to your door.</p>
  <div class="btn btn-blue" style="left:126px;top:2670px;width:176px;">Start Your Team Order</div>
  <div class="ph" role="img" aria-label="Two dark jerseys with yellow accents over a yellow paint stroke" style="left:625px;top:2395px;width:450px;height:375px;background:radial-gradient(ellipse at 55% 50%,#2b3440 0%,#3b4450 40%,#f2c230 62%,rgba(255,255,255,0) 75%);"></div>
</section>

<section class="brands">
  <h2 class="h2 abs" style="left:0;right:0;top:2832px;text-align:center;">Brands You Trust</h2>
  <div class="brand-badge" style="left:164px;border-color:#c58bd8;"><span class="dot" style="background:#8a5ad8;"></span>Kestrix</div>
  <div class="brand-badge" style="left:345px;border-color:#6fbf8a;"><span class="dot" style="background:#3f9d5d;"></span>Lumiva</div>
  <div class="brand-badge" style="left:525px;border-color:#d96060;">Tallo</div>
  <div class="brand-badge" style="left:706px;border-color:#e8c46a;"><span class="dot" style="background:#e08c2f;"></span>Ferno</div>
  <div class="brand-badge" style="left:886px;border-color:#e07a9a;"><span class="dot" style="background:#d4436b;"></span>Zuvia</div>
</section>

<section class="cta">
  <div class="ph" role="img" aria-label="Team in red and white kits celebrating with a trophy" style="left:178px;top:3125px;width:370px;height:335px;background:linear-gradient(180deg,#ffffff 0%,#e8e5e2 25%,#c94a4a 50%,#2c2c30 80%,#ffffff 100%);"></div>
  <h2 class="h2 abs" style="left:597px;top:3200px;width:450px;">Ready To Gear Up<br>Your Team?</h2>
  <p class="para abs" style="left:597px;top:3300px;width:420px;">It's time to elevate your team's performance and style with custom sports apparel designed just for you. Whether you need full team uniforms, personalized shirts, or unique gear, our easy-to-use tools and high-quality products make the process seamless.</p>
  <div class="btn btn-blue" style="left:597px;top:3383px;width:178px;">Design Custom Uniform</div>
  <div class="btn btn-red" style="left:782px;top:3383px;width:158px;">Create Custom Shirt</div>
</section>

<footer class="site-footer">
  <div class="brand" style="left:0;right:0;top:100px;justify-content:center;font-size:36px;color:var(--white);">
    <span class="mark" style="width:30px;height:30px;background:var(--red);"></span>
    <span>Wren Sporting Goods</span>
  </div>
  <nav class="footer-nav">
    <span>Home</span><span>Locker Room</span><span>Custom Uniforms</span><span>Custom Shirt Creator</span><span>Brands</span><span>About Us</span>
  </nav>
  <div class="socials">
    <span aria-label="Social profile one"></span><span aria-label="Social profile two"></span><span aria-label="Social profile three"></span><span aria-label="Social profile four"></span><span aria-label="Social profile five"></span>
  </div>
  <div class="footer-rule"></div>
  <div class="copyright">© 2025 Wren Sporting Goods. All rights reserved.</div>
</footer>
<div class="to-top" aria-label="Back to top"><svg width="12" height="12" viewBox="0 0 12 12" fill="none" stroke="#fff" stroke-width="2"><path d="M3 8l3-3 3 3"/></svg></div>

</body>
</html>
```